Start up in business consultancy needs a business card

We need the business card's layout (we have already the logo). Our business is concerned on consultancy services delivered to companies on the matter of sustainability. Business card should be enough essentials and professional style.

Side A with the following info:
logo + a space for the claim (still to identify) + website of the company

Side B with the following info:
Name of business card holder + title of the business card holder + address of the company + space for mobile number, phone number, fax number + e-mail of business card holder + graphic details around.

Target Market(s)

Business of any sector

Industry/Entity Type

Business Service

Contact Information for Business Card

Name of the company:
Lumeroca srl
Società Benefit

Address of the company:
Via Pescoli, 7
21099 - Gallarate (VA)

Website:
www.lumeroca-esempio.it

Name of the BC' holder:
Ettore Valsenzi

Title:
Co-fondatore

Email:
ettore@lumeroca-esempio.it

Mobile:
+39 351 602 7415
Phone:
+39 351 602 7415
Fax:
+39 351 602 7415

Font styles to use
Other font styles liked:
• new gothic

```html
<!DOCTYPE html>
<html lang="it">
<head>
<meta charset="utf-8">
<title>Lumeroca srl – Biglietto da visita</title>
<link href="https://fonts.googleapis.com/css2?family=Questrial&display=swap" rel="stylesheet">
<style>
  :root {
    --stage: #2c2c2c;
    --card: #f4f4f4;
    --card-edge: #e6e6e6;
    --brand-blue: #0a78c2;
    --ink: #2a2a2a;
    --ink-soft: #3c3c3c;
    --white: #ffffff;
  }
  * { box-sizing: border-box; margin: 0; padding: 0; }
  html, body { width: 1200px; height: 834px; overflow: hidden; }
  body {
    background: var(--stage);
    font-family: "Questrial", "Century Gothic", sans-serif;
    position: relative;
  }
  .card {
    position: absolute;
    top: 245px;
    width: 540px;
    height: 344px;
    background: linear-gradient(135deg, var(--white) 0%, var(--card) 60%, var(--card-edge) 100%);
    box-shadow: 0 10px 30px rgba(0,0,0,.45);
    overflow: hidden;
  }
  .card--front { left: 40px; }
  .card--back { left: 620px; }

  .brand {
    display: flex;
    align-items: center;
    gap: 12px;
    color: var(--brand-blue);
  }
  .brand__dot {
    width: 54px; height: 54px;
    border: 3px solid var(--brand-blue);
    border-radius: 50%;
    flex: none;
  }
  .brand__name { font-size: 30px; letter-spacing: .5px; }

  .card--front .brand {
    position: absolute;
    left: 50%; top: 92px;
    transform: translateX(-50%);
  }
  .web-band {
    position: absolute;
    left: 0; right: 0;
    top: 232px; height: 38px;
    background: var(--brand-blue);
    color: var(--white);
    font-size: 15px;
    display: flex; align-items: center; justify-content: center;
    letter-spacing: .3px;
  }

  .card--back .brand {
    position: absolute;
    left: 38px; top: 196px;
  }
  .card--back .brand__dot { width: 48px; height: 48px; }
  .card--back .brand__name { font-size: 27px; }

  .contact {
    position: absolute;
    left: 300px; top: 66px;
    color: var(--ink-soft);
    font-size: 13px;
    line-height: 1.35;
  }
  .contact__name { color: var(--ink); font-size: 16px; letter-spacing: .2px; }
  .contact__role { color: var(--brand-blue); font-size: 14px; margin-bottom: 12px; }
  .contact__address { margin-bottom: 14px; }
  .contact__list { list-style: none; }
  .contact__list li { display: flex; align-items: center; gap: 10px; height: 19px; white-space: nowrap; }
  .contact__list svg { width: 12px; height: 12px; flex: none; stroke: var(--ink); fill: none; stroke-width: 1.4; }
</style>
</head>
<body>

<section class="card card--front" aria-label="Fronte">
  <div class="brand">
    <span class="brand__dot"></span>
    <span class="brand__name">lumeroca</span>
  </div>
  <div class="web-band">www.lumeroca-esempio.it</div>
</section>

<section class="card card--back" aria-label="Retro">
  <div class="brand">
    <span class="brand__dot"></span>
    <span class="brand__name">lumeroca</span>
  </div>

  <div class="contact">
    <p class="contact__name">Ettore Valsenzi</p>
    <p class="contact__role">Co-fondatore</p>
    <p class="contact__address">Via Pescoli, 7<br>21099 - Castelvanno (VX)</p>
    <ul class="contact__list">
      <li>
        <svg viewBox="0 0 12 12" aria-label="Cellulare"><rect x="3" y="0.8" width="6" height="10.4" rx="1"/><line x1="5.2" y1="9.4" x2="6.8" y2="9.4"/></svg>
        +39 351 602 7415
      </li>
      <li>
        <svg viewBox="0 0 12 12" aria-label="Telefono"><path d="M1 4.5 Q6 1 11 4.5 L10 6 L8 5 L8 4 Q6 3.3 4 4 L4 5 L2 6 Z"/><rect x="3" y="7" width="6" height="4" rx="0.8"/></svg>
        +39 351 602 7415
      </li>
      <li>
        <svg viewBox="0 0 12 12" aria-label="Fax"><rect x="3" y="1" width="6" height="3.5"/><rect x="1" y="4.5" width="10" height="5" rx="0.8"/><rect x="3" y="8" width="6" height="3"/></svg>
        +39 351 602 7415
      </li>
      <li>
        <svg viewBox="0 0 12 12" aria-label="E-mail"><rect x="1" y="2.5" width="10" height="7"/><polyline points="1,2.5 6,6.5 11,2.5"/></svg>
        ettore@lumeroca-esempio.it
      </li>
    </ul>
  </div>
</section>

</body>
</html>
```